Business Card Design

I do estate sales and would like business card to reflect look and feel of attached logo. I also have copy of logo in .eps and .tif if you need that instead of .jpeg.
Updates

sorry for the delay in reviewing these designs. I will pick one by tomorrow. Here are the absolutes: *must have tagline (we find good homes for your treasures *must use blue and green *must be horizontal *nothing too fancy please submit your best and final. Thanks so much!

Industry/Entity Type

Business

Contact Information for Business Card

Nora Platt

DEALS by NORA
We find good homes for your treasures.

Specializing in one to three-day sales
o (no sale too big or too small)
• Home and garage organizing
• Home Clean-out

Call Nora Platt at 202-555-0187
to schedule.

```html
<!DOCTYPE html>
<html lang="en">
<head>
<meta charset="utf-8">
<title>Deals by Nora – Business Card</title>
<link href="https://fonts.googleapis.com/css2?family=Tinos:wght@400;700&display=swap" rel="stylesheet">
<style>
  :root {
    --page-bg: #e9e4dc;
    --navy-deep: #1c1f4a;
    --navy-mid: #262c6e;
    --royal-glow: #3a3f9c;
    --text-white: #ffffff;
    --band-green: #1e8f47;
    --band-line: #ffffff;
  }
  * { margin: 0; padding: 0; box-sizing: border-box; }
  html, body {
    width: 1200px;
    height: 900px;
    overflow: hidden;
    background: var(--page-bg);
  }
  .canvas {
    position: relative;
    width: 1200px;
    height: 900px;
  }
  .business-card {
    position: absolute;
    left: 100px;
    top: 160px;
    width: 1000px;
    height: 580px;
    overflow: hidden;
    background: radial-gradient(ellipse 60% 75% at 55% 45%, var(--royal-glow) 0%, var(--navy-mid) 50%, var(--navy-deep) 100%);
    font-family: "Tinos", "Times New Roman", serif;
    color: var(--text-white);
    box-shadow: 0 4px 14px rgba(0,0,0,0.25);
  }
  .house-backdrop {
    position: absolute;
    left: 320px;
    top: 110px;
    width: 520px;
    height: 360px;
    background: radial-gradient(ellipse at 50% 45%, rgba(70,80,150,0.35) 0%, rgba(40,46,110,0.15) 55%, rgba(0,0,0,0) 80%);
  }
  .brand-name {
    position: absolute;
    left: 60px;
    top: 120px;
    font-size: 38px;
    font-weight: 700;
    line-height: 1.2;
    color: var(--text-white);
    white-space: nowrap;
  }
  .contact {
    position: absolute;
    right: 54px;
    top: 40px;
    text-align: right;
    font-weight: 700;
  }
  .contact-name { font-size: 48px; line-height: 1.2; }
  .contact-phone {
    font-size: 36px;
    line-height: 1.4;
    display: inline-flex;
    align-items: center;
    gap: 10px;
  }
  .phone-icon { width: 30px; height: 26px; }
  .services {
    position: absolute;
    left: 626px;
    top: 236px;
    list-style: none;
    font-size: 22px;
    font-weight: 700;
  }
  .services li { margin-bottom: 19px; }
  .services li::before { content: "\2022"; margin-right: 6px; }
  .tagline {
    position: absolute;
    left: 0;
    width: 100%;
    top: 420px;
    text-align: center;
    font-size: 31px;
    font-weight: 700;
    line-height: 1.22;
    padding-left: 120px;
  }
  .footer-band {
    position: absolute;
    left: 0;
    bottom: 0;
    width: 1000px;
    height: 100px;
  }
</style>
</head>
<body>
<main class="canvas">
  <section class="business-card" aria-label="Deals by Nora business card">
    <div class="house-backdrop" role="img" aria-label="Faint photograph of a house with trees behind it"></div>

    <p class="brand-name">DEALS by NORA</p>

    <div class="contact">
      <div class="contact-name">Nora Platt</div>
      <div class="contact-phone">
        <svg class="phone-icon" viewBox="0 0 30 26" aria-hidden="true">
          <path d="M2 9 Q15 0 28 9 L26 13 L21 11 L20 7 Q15 5 10 7 L9 11 L4 13 Z" fill="#fff"/>
          <path d="M8 13 L22 13 L27 24 L3 24 Z" fill="#fff"/>
          <circle cx="15" cy="18.5" r="3" fill="#262c6e"/>
        </svg>
        <span>202-555-0187</span>
      </div>
    </div>

    <ul class="services">
      <li>Home and garage organizing</li>
      <li>Home Clean-out</li>
    </ul>

    <p class="tagline">We find good homes for your treasures.<br>Specializing in one to three-day sales</p>

    <svg class="footer-band" viewBox="0 0 1000 100" preserveAspectRatio="none" aria-hidden="true">
      <path d="M0 82 L700 22 Q720 20 745 20 L1000 20 L1000 100 L0 100 Z" fill="var(--band-green)"/>
      <path d="M0 82 L700 22 Q720 20 745 20 L1000 20" fill="none" stroke="var(--band-line)" stroke-width="4"/>
    </svg>
  </section>
</main>
</body>
</html>
```